" SOU MÉDICO ORTOPEDISTA COM ESPECIALIZAÇÃO EM CIRURGIA DO JOELHO E DO QUADRIL. REALIZO ATENDIMENTOS AMBULATORIAIS E CIRURGICOS NESTAS ARÉAS PRINCIPALMENTE. "

```html
<!DOCTYPE html>
<html lang="pt-BR">
<head>
<meta charset="UTF-8">
<title>Cartão de visita — Marcelo Tavares Brandão</title>
<link rel="stylesheet" href="https://fonts.googleapis.com/css2?family=Open+Sans:wght@400;600;700&display=swap">
<style>
  :root {
    --page-bg: #eceef1;
    --card-white: #ffffff;
    --navy-dark: #132a47;
    --navy: #1e3f66;
    --accent-blue: #2f86c9;
    --accent-light: #4fa6e0;
    --brand-grey: #4a5a6e;
    --brand-blue: #2a5d8f;
    --text-white: #ffffff;
    --text-soft: #d5e2f0;
  }
  * { box-sizing: border-box; margin: 0; padding: 0; }
  html, body {
    width: 1200px; height: 1200px; overflow: hidden;
    background: var(--page-bg);
    font-family: "Open Sans", Arial, sans-serif;
  }
  .canvas {
    position: relative; width: 1200px; height: 1200px;
    display: flex; flex-direction: column; align-items: center; justify-content: center; gap: 80px;
  }
  .card {
    position: relative; width: 760px; height: 420px; border-radius: 44px; overflow: hidden;
    box-shadow: 0 6px 20px rgba(20, 40, 70, 0.12);
  }
  /* Front */
  .card-front {
    background: var(--card-white);
    display: flex; flex-direction: column; align-items: center; justify-content: center; gap: 22px;
  }
  .brand-mark {
    width: 86px; height: 86px; border-radius: 50%;
    border: 10px solid #a9b3bd;
  }
  .brand-name {
    font-size: 40px; font-weight: 400; letter-spacing: 1px; text-transform: uppercase;
    color: var(--brand-grey);
  }
  .brand-specialty {
    margin-top: -14px;
    font-size: 15px; font-weight: 400; letter-spacing: 5px; text-transform: uppercase;
    color: var(--brand-blue);
  }
  /* Back */
  .card-back {
    background: linear-gradient(120deg, var(--navy-dark) 0%, var(--navy) 100%);
  }
  .back-band { position: absolute; left: 0; bottom: 0; width: 760px; height: 120px; }
  .back-mark {
    position: absolute; right: 110px; top: 70px;
    width: 170px; height: 170px; border-radius: 50%;
    border: 16px solid #9aa6b2;
  }
  .contact-block {
    position: absolute; left: 70px; top: 150px; color: var(--text-white);
  }
  .person-name { font-size: 22px; font-weight: 700; text-transform: uppercase; }
  .person-role { font-size: 22px; font-weight: 700; text-transform: uppercase; margin-bottom: 26px; }
  .contact-list { list-style: none; display: flex; flex-direction: column; gap: 8px; }
  .contact-item {
    display: flex; align-items: flex-start; gap: 12px;
    font-size: 16px; color: var(--text-soft); line-height: 1.35;
  }
  .contact-icon { width: 18px; height: 18px; flex: none; margin-top: 2px; fill: var(--text-white); }
  .icon-dot { width: 16px; height: 16px; border-radius: 50%; background: var(--text-white); flex: none; margin: 3px 1px 0; }
</style>
</head>
<body>
<main class="canvas">
  <section class="card card-front" aria-label="Frente do cartão">
    <div class="brand-mark" aria-hidden="true"></div>
    <h1 class="brand-name">Marcelo Tavares Brandão</h1>
    <p class="brand-specialty">Ortopedia e Traumatologia</p>
  </section>

  <section class="card card-back" aria-label="Verso do cartão">
    <svg class="back-band" viewBox="0 0 760 120" preserveAspectRatio="none" aria-hidden="true">
      <defs>
        <linearGradient id="bandGradient" x1="0" y1="0" x2="1" y2="0">
          <stop offset="0" stop-color="#1e4f86"/>
          <stop offset="0.55" stop-color="#2f86c9"/>
          <stop offset="1" stop-color="#4fa6e0"/>
        </linearGradient>
      </defs>
      <path d="M0 80 C 250 95, 520 60, 760 10 L760 120 L0 120 Z" fill="url(#bandGradient)"/>
      <path d="M0 95 C 260 108, 520 78, 760 35 L760 120 L0 120 Z" fill="#1a4270" opacity="0.55"/>
    </svg>

    <div class="back-mark" aria-hidden="true"></div>

    <div class="contact-block">
      <p class="person-name">Nome Sobrenome</p>
      <p class="person-role">Função</p>
      <ul class="contact-list">
        <li class="contact-item">
          <svg class="contact-icon" viewBox="0 0 24 24" aria-hidden="true"><path d="M6.6 10.8a15.1 15.1 0 0 0 6.6 6.6l2.2-2.2a1 1 0 0 1 1-.25 11.4 11.4 0 0 0 3.6.57 1 1 0 0 1 1 1V20a1 1 0 0 1-1 1A17 17 0 0 1 3 4a1 1 0 0 1 1-1h3.5a1 1 0 0 1 1 1c0 1.25.2 2.45.57 3.57a1 1 0 0 1-.25 1z"/></svg>
          <span>(00)0000-0000</span>
        </li>
        <li class="contact-item">
          <span class="icon-dot" aria-hidden="true"></span>
          <span>(00)0000-0000</span>
        </li>
        <li class="contact-item">
          <svg class="contact-icon" viewBox="0 0 24 24" aria-hidden="true"><path d="M12 2a7 7 0 0 0-7 7c0 5.25 7 13 7 13s7-7.75 7-13a7 7 0 0 0-7-7zm0 9.5A2.5 2.5 0 1 1 12 6.5a2.5 2.5 0 0 1 0 5z"/></svg>
          <span>rua sem nome,00 , Bairro Sem Nome<br>Cidade Sem Nome</span>
        </li>
      </ul>
    </div>
  </section>
</main>
</body>
</html>
```